I'm an electrician and the name of my company is called Brisk 'N' Bright Electrical. I require a professional business card that speaks to my clients, I also need it to be innovative and modern. We do maintenance & service work for domestic and commercial premises.

Industry/Entity Type

Electrical

Contact Information for Business Card

Must have the name of my company Brisk 'N' Bright Electrical, my name Darren Kolovich and my contact details 0427 318 592 and company email address Brisknbrightelectrical@quillpost.example and/or website Brisknbrightelectrical.example.au

Logo Text

Brisk 'N' Bright Electrical (If possible)

Colors
33a6d7
0592cd
3176b5

```html
<!DOCTYPE html>
<html lang="en">
<head>
<meta charset="utf-8">
<title>Brisk 'N' Bright Electrical — Business Card</title>
<link rel="stylesheet" href="https://fonts.googleapis.com/css2?family=Arimo:wght@400;700&display=swap">
<style>
  :root {
    --card-blue: #3176b5;
    --accent-blue: #0592cd;
    --sky-blue: #33a6d7;
    --paper: #ffffff;
    --ink: #1a1a1a;
    --backdrop: #e9ecef;
  }
  * { box-sizing: border-box; margin: 0; padding: 0; }
  html, body {
    width: 1200px; height: 900px; overflow: hidden;
    background: var(--backdrop);
    font-family: "Arimo", Arial, sans-serif;
  }
  .canvas {
    width: 1200px; height: 900px;
    display: flex; flex-direction: column;
    align-items: center; justify-content: center; gap: 40px;
  }
  .card {
    position: relative;
    width: 680px; height: 388px;
    overflow: hidden;
    box-shadow: 0 6px 18px rgba(0,0,0,0.18);
  }
  .card--front { background: var(--card-blue); display: flex; align-items: center; justify-content: center; }
  .card--back { background: var(--card-blue); }
  .brand {
    display: flex; align-items: center; gap: 14px;
    color: var(--paper); font-weight: 700; font-size: 40px; letter-spacing: 0.5px;
    white-space: nowrap;
  }
  .brand__dot {
    width: 30px; height: 30px; border-radius: 50%;
    background: var(--paper); flex: none;
  }
  .card__wave { position: absolute; inset: 0; width: 100%; height: 100%; }
  .card--back .brand {
    position: absolute; left: 36px; top: 118px; font-size: 30px; gap: 12px;
  }
  .card--back .brand__dot { width: 26px; height: 26px; }
  .holder {
    position: absolute; left: 60px; top: 318px;
    font-weight: 700; font-size: 22px; letter-spacing: 1px; color: var(--ink);
  }
  .contacts {
    position: absolute; right: 30px; top: 170px;
    list-style: none; display: flex; flex-direction: column; gap: 10px;
    font-size: 15px; color: var(--ink); text-align: right;
  }
  .contacts li { display: flex; align-items: center; justify-content: flex-end; gap: 8px; }
  .contacts svg { width: 16px; height: 16px; flex: none; }
</style>
</head>
<body>
<main class="canvas">
  <section class="card card--front" aria-label="Card front">
    <div class="brand"><span class="brand__dot"></span>Brisk 'N' Bright</div>
  </section>

  <section class="card card--back" aria-label="Card back">
    <svg class="card__wave" viewBox="0 0 680 388" preserveAspectRatio="none" aria-hidden="true">
      <path d="M0 300 C150 270 300 190 420 110 C480 70 530 25 570 0 L680 0 L680 388 L0 388 Z" fill="#ffffff"/>
    </svg>
    <div class="brand"><span class="brand__dot"></span>Brisk 'N' Bright</div>
    <p class="holder">Darren Kolovich</p>
    <ul class="contacts">
      <li>0427 318 592
        <svg viewBox="0 0 16 16" aria-hidden="true"><rect x="4" y="1" width="8" height="14" rx="1.5" fill="none" stroke="#0592cd" stroke-width="1.4"/><circle cx="8" cy="12.5" r="0.9" fill="#0592cd"/></svg>
      </li>
      <li>Brisknbrightelectrical.example.au
        <svg viewBox="0 0 16 16" aria-hidden="true"><circle cx="8" cy="8" r="6.5" fill="#0592cd"/><path d="M1.5 8h13M8 1.5c-3 3.5-3 9.5 0 13M8 1.5c3 3.5 3 9.5 0 13" stroke="#fff" stroke-width="0.9" fill="none"/></svg>
      </li>
      <li>Brisknbrightelectrical@quillpost.example
        <svg viewBox="0 0 16 16" aria-hidden="true"><rect x="1" y="3" width="14" height="10" fill="#0592cd"/><path d="M1 3l7 5.5L15 3" stroke="#fff" stroke-width="1.1" fill="none"/></svg>
      </li>
    </ul>
  </section>
</main>
</body>
</html>
```